"Lantern Field" Play - Poster Design for Theatre Group

We are an amateur theatre group based in Geneva, Switzerland. We take pride in eye-catching posters for our shows, which are printed in various sizes.
This design will be for a play in March 2016. The play is called "Lantern Field", and it's a Harwick Medal winner from Morgan Pellew-Strand. The play is about a couple who have everything a family could want, until they lose a child in a life-shattering accident that turns their world upside down. The play charts the couple's bittersweet search to find each other and to find comfort.
Most importantly, we want a design that will make people want to see the show. We don't want to give away the plot or be too heavy-handed about death, but we want it to be clear that it's not a comedy (although there are some lighter moments!).
Attached you will find a template for the poster. This simply has our group name and logo in the top right corner: (Lakeside Stage Players Circle presents).
You may change the color of both the text and the logo, but please do not change the font, size, or location.
Here is the information that needs to be on the poster, wherever you see fit:
play title: Lantern Field
author byline: by Morgan Pellew-Strand
director line: directed by Ned Variscombe
tagline: How do you keep it together when your whole world's fallen apart?
dates and times:
1-5 March 2016
(Tue-Fri 20:00, Sat 19:00)
location:
Théâtre du Vieux Moulin
Eaux-Vives, Geneva
websites:
www.lspc.ch
www.scenesauboulevard.ch
Technical Details:
Any font or combination of fonts is acceptable. The largest text should be the play title. The author's name must be at least 50% of the title font size.
For this competition, we would like the version with A3 proportions, which will also be used at F4 (89.5 x 128 cm) and A5 sizes (14.8 x 21 cm). Therefore no text should be below 9pt at A5.
However, from the winning designer we will also need repurposed sizes of the same design. Here is a comprehensive list of the sizes we will need.
1) A3 print poster. Artwork should be 300dpi, CMYK, sent with a 1mm bleed all round, to specification PDF/X-1A:2001. We will need this image in PDF format in addition to the default Artmarketly formats.
2) Friendora advert picture. 1200px by 628px, RGB jpeg. This must comply with Friendora’s restrictions on amount of text, which is no more than 20% of area taken up by text.(https://www.friendora.example/ads/tools/text_overlay).
Because of these restrictions it is sufficient to include just the title and the author's name in this version.
3) Friendora cover picture: 851px by 314px. RGB jpeg. It is sufficient to include just the title and the author's name in this version.
4) Web banner. 1000px by 300px. RGB jpeg. This version should include just the main image(s), no text.

```html
<!DOCTYPE html>
<html lang="en">
<head>
<meta charset="utf-8">
<title>Lantern Field – Lakeside Stage Players Circle</title>
<link href="https://fonts.googleapis.com/css2?family=Pathway+Gothic+One&family=Roboto+Condensed:wght@400;700&display=swap" rel="stylesheet">
<style>
  :root {
    --backdrop: #d6dad6;
    --paper: #f4e2d6;
    --teal: #12a4bb;
    --pink: #e5466f;
    --crimson: #a3214c;
    --deep-teal: #1d6f86;
    --mauve: #7c5d5f;
    --ink: #7a5a5c;
  }
  * { box-sizing: border-box; margin: 0; padding: 0; }
  html, body { width: 960px; height: 1200px; overflow: hidden; }
  body {
    background: var(--backdrop);
    display: flex; align-items: center; justify-content: center;
    font-family: "Roboto Condensed", "Arial Narrow", sans-serif;
  }
  .poster {
    position: relative;
    width: 820px; height: 1160px;
    background: var(--paper);
    box-shadow: 0 2px 10px rgba(0,0,0,.15);
    overflow: hidden;
  }
  .presenter {
    position: absolute; top: 42px; right: 44px;
    display: flex; align-items: center; gap: 14px;
    color: var(--mauve);
  }
  .presenter-name {
    text-align: right; font-weight: 700; font-size: 21px; line-height: 1.15;
  }
  .presenter-mark {
    width: 78px; height: 78px; border-radius: 50%;
    border: 4px solid var(--mauve);
  }
  .key-art {
    position: absolute; left: 200px; top: 170px;
    width: 480px; height: 440px;
  }
  .title {
    position: absolute; left: 0; right: 0; top: 628px;
    text-align: center; white-space: nowrap;
    font-family: "Pathway Gothic One", "Arial Narrow", sans-serif;
    font-weight: 400;
    font-size: 196px; line-height: 0.9;
  }
  .title-word-group {
    display: inline-block;
    transform: scaleX(0.78);
    transform-origin: center;
  }
  .title-first { color: var(--teal); }
  .title-second { color: var(--pink); }
  .tagline {
    position: absolute; left: 82px; right: 62px; top: 850px;
    background: var(--mauve); color: var(--paper);
    text-align: center; text-transform: uppercase;
    font-weight: 700; font-size: 22px; line-height: 1.3;
    padding: 8px 10px;
  }
  .credits {
    position: absolute; left: 0; right: 0; top: 940px;
    text-align: center; white-space: nowrap;
    font-family: "Pathway Gothic One", "Arial Narrow", sans-serif;
    text-transform: uppercase;
  }
  .credit-label { font-size: 30px; }
  .credit-name { font-size: 44px; }
  .credit-author { color: var(--crimson); }
  .credit-director { color: var(--deep-teal); margin-left: 12px; }
  .details {
    position: absolute; left: 0; right: 0; top: 1008px;
    text-align: center; color: var(--ink);
    font-size: 20px; line-height: 1.3; text-transform: uppercase;
  }
  .details .sites { text-transform: none; letter-spacing: .5px; }
</style>
</head>
<body>
  <main class="poster">
    <header class="presenter">
      <p class="presenter-name">Lakeside Stage<br>Players Circle<br>presents</p>
      <span class="presenter-mark" aria-hidden="true"></span>
    </header>

    <svg class="key-art" viewBox="0 0 480 440" role="img" aria-label="Key art: two overlapping speech bubbles, teal and pink, each holding a silhouetted head in profile facing the other">
      <defs>
        <linearGradient id="keyArtTone" x1="0" y1="0" x2="1" y2="0">
          <stop offset="0" stop-color="#12a4bb"/>
          <stop offset="1" stop-color="#e5466f"/>
        </linearGradient>
      </defs>
      <rect width="480" height="440" rx="30" fill="url(#keyArtTone)" opacity="0.85"/>
    </svg>

    <h1 class="title"><span class="title-word-group"><span class="title-first">LANTERN</span><span class="title-second">FIELD</span></span></h1>

    <p class="tagline">How do you keep it together<br>when your whole world's fallen apart?</p>

    <p class="credits"><span class="credit-author"><span class="credit-label">by </span><span class="credit-name">Morgan Pellew-Strand</span></span><span class="credit-director"><span class="credit-label">directed by </span><span class="credit-name">Ned Variscombe</span></span></p>

    <div class="details">
      <p><strong>1-5 March 2016 (Tue-Fri 20:00, Sat 19:00)</strong></p>
      <p>Théâtre du Vieux Moulin, Eaux-Vives, Geneva</p>
      <p class="sites">www.lspc.ch &nbsp;|&nbsp; www.scenesauboulevard.ch</p>
    </div>
  </main>
</body>
</html>
```